Looking for something sharp classy and with an edge for an advanced civil construction business
Something that says professional
nothing too DARK

Target Market(s)

mining companies council civil contractors concrete works

Industry/Entity Type

Construction

Contact Information for Business Card

Brindle Civil Constructions
brindlecivilconstruction@quokkamail.com
Tavi Marlowe
0418275936

Font styles to use
Serif
Sans Serif

Colors
0455a3
0592cd
85cae6
000000
919191

Requirements
Must have
• On the back of the card must have
down the bottom small print email logo phone number

Should not have
• follow us on facebook
Brindle Civil Constructions

follow us on instagram
BRINDLECIVILCONSTRUCTIONS

```html
<!DOCTYPE html>
<html lang="en">
<head>
<meta charset="utf-8">
<title>Brindle Civil Constructions – Business Card</title>
<link rel="stylesheet" href="https://fonts.googleapis.com/css2?family=Bebas+Neue&family=Caladea&family=Arimo:wght@400;700&display=swap">
<style>
  :root {
    --blue-deep: #0455a3;
    --blue-mid: #0592cd;
    --blue-light: #85cae6;
    --black: #000000;
    --grey: #919191;
    --grey-text: #959595;
    --charcoal: #333132;
    --contact-blue: #1a9ddc;
    --page: #ffffff;
    --label: #222222;
  }
  html, body {
    margin: 0;
    padding: 0;
    width: 1055px;
    height: 1200px;
    overflow: hidden;
    background: var(--page);
  }
  .sheet {
    position: relative;
    width: 1055px;
    height: 1200px;
  }
  .side-label {
    position: absolute;
    left: 0;
    width: 1055px;
    text-align: center;
    font-family: "Arimo", Arial, sans-serif;
    font-size: 27px;
    color: var(--label);
    margin: 0;
    line-height: 1;
  }
  .side-label--front { top: 4px; }
  .side-label--back { top: 626px; }
  .card {
    position: absolute;
    left: 0;
    display: block;
  }
  .card--front { top: 48px; width: 1024px; height: 528px; }
  .card--back { top: 671px; width: 1055px; height: 529px; }
  .front-title {
    font-family: "Bebas Neue", "Oswald", sans-serif;
    font-size: 112px;
    fill: var(--grey);
  }
  .holder-name {
    font-family: "Caladea", "Cambria", serif;
    font-size: 80px;
    fill: var(--grey-text);
    stroke: #b9b9b9;
    stroke-width: 0.8;
    filter: drop-shadow(2px 3px 2px rgba(0,0,0,0.35));
  }
  .contact-line {
    font-family: "Arimo", Arial, sans-serif;
    font-size: 32px;
    fill: var(--contact-blue);
  }
  .brand-name {
    font-family: "Arimo", Arial, sans-serif;
    font-weight: 700;
    fill: #ffffff;
  }
  .brand-name--main { font-size: 30px; letter-spacing: 1px; }
  .brand-name--sub { font-size: 12px; }
</style>
</head>
<body>
<main class="sheet">
  <p class="side-label side-label--front">Front</p>

  <svg class="card card--front" viewBox="0 0 1024 528" xmlns="http://www.w3.org/2000/svg">
    <defs>
      <linearGradient id="front-base" x1="0" y1="0" x2="1" y2="0.4">
        <stop offset="0" stop-color="var(--blue-deep)"/>
        <stop offset="0.6" stop-color="#0559a8"/>
        <stop offset="1" stop-color="#0a6fbf"/>
      </linearGradient>
      <linearGradient id="brick-band" x1="0" y1="0" x2="0" y2="1">
        <stop offset="0" stop-color="#0a66b4" stop-opacity="0"/>
        <stop offset="0.5" stop-color="#2d7fc1" stop-opacity="0.6"/>
        <stop offset="1" stop-color="#4a93cc" stop-opacity="0.85"/>
      </linearGradient>
      <radialGradient id="brick-corner" cx="1" cy="0" r="0.55">
        <stop offset="0" stop-color="#3f8ccb" stop-opacity="0.8"/>
        <stop offset="1" stop-color="#0559a8" stop-opacity="0"/>
      </radialGradient>
    </defs>
    <rect class="front-base" width="1024" height="528" fill="url(#front-base)"/>
    <rect class="brick-area brick-area--corner" x="560" y="0" width="464" height="260" fill="url(#brick-corner)" role="img" aria-label="Light blue brick pattern fading in at the top right"/>
    <rect class="brick-area brick-area--base" x="0" y="330" width="1024" height="198" fill="url(#brick-band)" role="img" aria-label="Light blue brick pattern along the bottom of the card"/>
    <text class="front-title" x="64" y="303" textLength="929" lengthAdjust="spacingAndGlyphs">BRINDLE CIVIL CONTRUCTION</text>
  </svg>

  <p class="side-label side-label--back">Back</p>

  <svg class="card card--back" viewBox="0 0 1055 529" xmlns="http://www.w3.org/2000/svg">
    <rect class="back-base" width="1055" height="529" fill="var(--grey)"/>
    <g class="brand-block">
      <rect x="764" y="0" width="291" height="65" fill="var(--black)"/>
      <text class="brand-name brand-name--main" x="772" y="33">BRINDLE</text>
      <text class="brand-name brand-name--sub" x="772" y="55" textLength="277" lengthAdjust="spacingAndGlyphs">BUILDING AND CIVIL ENGINEERING LTD</text>
    </g>
    <text class="holder-name" x="527" y="289" text-anchor="middle" textLength="538" lengthAdjust="spacingAndGlyphs">Tavi Marlowe</text>
    <polygon class="footer-band" points="0,447 527,396 1055,456 1055,529 0,529" fill="var(--charcoal)"/>
    <text class="contact-line contact-line--phone" x="527" y="484" text-anchor="middle">Ph no: 0418275936</text>
    <text class="contact-line contact-line--email" x="527" y="516" text-anchor="middle" textLength="600" lengthAdjust="spacingAndGlyphs">brindlecivilconstruction@quokkamail.com</text>
  </svg>
</main>
</body>
</html>
```